Homepage web design

I need a homepage design that will be easy to build into a default Word Press theme. Basically, header, navigation, body with sidebar, and footer.

This website is for a small commercial real estate firm in the Washington DC, Maryland and Virginia market.

THIS IS NOT A HOUSING/RESIDENTIAL WEBSITE. PLEASE DO NOT ADD ANY PROPERTY SEARCH FUNCTIONALITY.

Target Market(s)

People looking for basic information about the team and services provided.

Industry/Entity Type

Real Estate

Requirements
Must have
• Professional look. Clean design.

```html
<!DOCTYPE html>
<html lang="en">
<head>
<meta charset="utf-8">
<title>Meridian Brokerage – Commercial Real Estate</title>
<link rel="stylesheet" href="https://fonts.googleapis.com/css2?family=Questrial&family=Cinzel:wght@400&display=swap">
<style>
:root{
  --bg:#ececec;
  --bg-dark:#e2e2e2;
  --green:#10995a;
  --green-dark:#0b7f48;
  --ink:#2b2b2b;
  --body:#555;
  --muted:#999;
  --line:#c9c9c9;
  --nav:#e4e4e4;
}
*{box-sizing:border-box;margin:0;padding:0}
html,body{width:1200px;height:900px;overflow:hidden}
body{position:relative;background:linear-gradient(#f3f3f3,var(--bg) 40%,#e9e9e9);font-family:Arial,Helvetica,sans-serif;color:var(--body)}
.abs{position:absolute}
.brand{left:70px;top:30px;font-family:"Questrial",sans-serif;font-size:24px;color:var(--green);letter-spacing:.5px}
.brand-mark{display:inline-block;width:10px;height:10px;background:var(--green);margin-right:8px;vertical-align:middle}
.contact-bar{right:72px;top:44px;text-align:right;font-family:"Questrial",sans-serif;font-size:11px;color:#555;letter-spacing:.6px;line-height:13px}
.contact-bar .phone{font-size:14px;color:#333;letter-spacing:1px}
.hero{left:69px;top:69px;width:1060px;height:293px;background:linear-gradient(180deg,#2f63b8 0%,#5f92d6 35%,#9fbde0 60%,#7c8a98 80%,#4b4f55 100%);overflow:hidden;box-shadow:0 4px 14px rgba(0,0,0,.25)}
.hero-dots{right:18px;top:10px;display:flex;gap:9px}
.hero-dots span{width:11px;height:11px;border-radius:50%;background:#333}
.hero-dots span.on{background:var(--green)}
.hero-title{left:756px;top:103px;font-family:"Cinzel",serif;font-size:30px;line-height:29px;color:#2a2a2a;letter-spacing:2px}
.feedback{left:1147px;top:218px;width:53px;height:65px;background:#f5f5f5;border:1px solid #bbb;border-right:0;border-radius:6px 0 0 6px}
.feedback span{position:absolute;left:20px;top:6px;writing-mode:vertical-rl;font-size:9px;letter-spacing:2px;color:#333}
.nav{left:69px;top:366px;width:1060px;height:43px;display:flex}
.nav a{flex:1;display:flex;align-items:center;justify-content:center;font-size:10px;letter-spacing:.8px;color:#333;text-decoration:none;background:linear-gradient(#f2f2f2,var(--nav));border-left:1px solid #bdbdbd}
.nav a.active{background:linear-gradient(var(--green),var(--green-dark));color:#fff;border-left:1px solid #fff}
.nav a:first-child{border-left:0}
.dropdown{left:247px;top:409px;width:177px;font-size:10px;text-align:center;letter-spacing:.6px}
.dropdown div{height:15px;line-height:15px;color:#333;background:#f4f4f4;border-bottom:1px solid #ccc}
.dropdown div.on{background:#2d2d2d;color:#fff}
.col{width:315px}
h2{font-family:"Questrial",sans-serif;font-weight:400;font-size:19px;line-height:20px;letter-spacing:1px;color:var(--ink)}
h3{font-size:10.5px;font-weight:bold;color:#333;margin-top:3px;letter-spacing:.4px;line-height:12px}
.txt{font-size:9.4px;line-height:10.5px;text-align:justify;color:#555;letter-spacing:.6px}
.more{display:block;text-align:right;font-size:10px;color:#333;margin-top:3px;letter-spacing:.3px}
.more.dim{color:#aaa}
.photo{height:65px;margin-top:8px}
.photo.team{background:linear-gradient(90deg,#cfd4da,#e8e2da 40%,#d6d8dc)}
.photo.tower{background:linear-gradient(180deg,#b9d2ee,#3f6fb5 50%,#1f3f78)}
.photo.news{background:linear-gradient(120deg,#d6e3f0,#8fb0d6 40%,#8a3e38 55%,#3b5f93)}
.card .txt{padding:0 18px;margin-top:12px;font-size:9px;line-height:9.6px;letter-spacing:.55px}
.card .more{margin-top:1px}
.footer{left:0;top:755px;width:1200px;height:120px;background:var(--bg-dark);border-top:1px solid #d0d0d0}
.divider{top:772px;width:1px;height:90px;background:var(--line)}
.foot-h{font-family:"Questrial",sans-serif;font-size:13px;line-height:14px;letter-spacing:1px;color:#333}
.foot-txt{font-size:8.4px;line-height:8.8px;color:var(--muted);text-align:justify;letter-spacing:.6px}
.quote-name{font-family:"Cinzel",serif;font-size:10px;line-height:11px;color:#333;margin-top:5px}
.quote-name small{font-family:Arial,sans-serif;font-size:8px;margin-left:18px;letter-spacing:.3px}
.social{display:flex;gap:12px;margin-top:3px;margin-left:4px}
.social span{width:34px;height:18px;border-radius:50%;background:#d9d9d9;border:1px solid #c4c4c4}
.social span.on{background:#1e3f86}
.fan{width:98px;height:18px;border:1px solid #aaa;border-radius:4px;background:#fff;font-size:7.5px;text-align:center;line-height:8px;padding-top:1px;color:#333;margin-top:3px;margin-left:-18px}
.copyright{left:73px;top:879px;font-size:9px;color:#333;letter-spacing:.3px}
.foot-brand{right:72px;top:878px;font-family:"Questrial",sans-serif;font-size:11px;color:var(--green)}
</style>
</head>
<body>
<header>
  <div class="abs brand"><span class="brand-mark"></span>Meridian Brokerage</div>
  <div class="abs contact-bar">
    <div>Any Questions? Call Us : <span class="phone">1800-555-014</span></div>
    <div>Support | FAQs | Sitemap</div>
  </div>
</header>

<section class="abs hero" role="img" aria-label="Photograph of a modern glass office building on a city street under blue sky">
  <div class="abs hero-dots"><span></span><span></span><span></span><span class="on"></span></div>
  <div class="abs hero-title">Service<br>You<br>Deserve</div>
</section>

<div class="abs feedback"><span>Feedback</span></div>

<nav class="abs nav">
  <a class="active">HOME</a><a class="active">ABOUT US</a><a>SERVICES</a><a>GALLERY</a><a>BLOG</a><a>CONTACT US</a>
</nav>
<div class="abs dropdown"><div>Company</div><div>Team</div><div class="on">News</div></div>

<section class="abs col" style="left:70px;top:431px">
  <h2>ADVANTAGES</h2><h3>Lorem Ipsum Dolor</h3>
  <p class="txt">Lorem Ipsum is simply dummy text of the printing and typesetting industry. Lorem Ipsum has been the industry's standard dummy text ever since the 1500s, when an unknown printer took a galley of type and scrambled it to make a type specimen book. It has survived not only five centuries, but also the leap into electronic typesetting, remaining essentially unchanged. It was popularised in the 1960s with the</p>
  <a class="more dim" style="margin-right:5px">Read More...</a>
</section>
<section class="abs col" style="left:442px;top:431px">
  <h2>MISSION</h2><h3>Lorem Ipsum Dolor</h3>
  <p class="txt">It is a long established fact that a reader will be distracted by the readable content of a page when looking at its layout. The point of using Lorem Ipsum is that it has a more-or-less normal distribution of letters, as opposed to using 'Content here, content here', making it look like readable English. Many desktop publishing packages and web page editors now use Lorem Ipsum as their default).</p>
  <a class="more">Read More...</a>
</section>
<section class="abs col" style="left:814px;top:431px">
  <h2>VISSION</h2><h3>Lorem Ipsum Dolor</h3>
  <p class="txt">Lorem Ipsum is simply dummy text of the printing and typesetting industry. Lorem Ipsum has been the industry's standard dummy text ever since the 1500s, when an unknown printer took a galley of type and scrambled it to make a type specimen book. It has survived not only five centuries, but also the leap into electronic typesetting, remaining essentially unchanged. It was popularised in the 1960s with the</p>
  <a class="more">Read More...</a>
</section>

<section class="abs col card" style="left:69px;top:564px;width:323px">
  <h2 style="margin-left:3px">WELCOME</h2>
  <div class="photo team" role="img" aria-label="Photograph of a business team meeting around a table"></div>
  <p class="txt">Lorem Ipsum is simply dummy text of the printing and typesetting industry. Lorem Ipsum has been the industry's standard dummy text ever since the 1500s, when an unknown printer took a galley of type and scrambled it to make a type specimen book. It has survived not only five centuries, but also the leap into electronic typesetting, remaining essentially unchanged. It was popularised in the 1960s with the release of transfer sheets containing Lorem Ipsum</p>
  <a class="more" style="margin-right:20px">Read More...</a>
</section>
<section class="abs col card" style="left:441px;top:564px;width:316px">
  <h2 style="margin-left:2px">WHAT WE DO</h2>
  <div class="photo tower" role="img" aria-label="Photograph of blue glass office towers"></div>
  <p class="txt">Lorem Ipsum is simply dummy text of the printing and typesetting industry. Lorem Ipsum has been the industry's standard dummy text ever since the 1500s, when an unknown printer took a galley of type and scrambled it to make a type specimen book. It has survived not only five centuries, but also the leap into electronic typesetting, remaining essentially unchanged. It was popularised in the 1960s with the release of transfer sheets containing Lorem Ipsum</p>
  <a class="more dim" style="margin-right:20px">Read More...</a>
</section>
<section class="abs col card" style="left:813px;top:564px;width:316px">
  <h2 style="margin-left:2px">WHAT'S NEW</h2>
  <div class="photo news" role="img" aria-label="Photograph of a modern angular office building"></div>
  <p class="txt">Lorem Ipsum is simply dummy text of the printing and typesetting industry. Lorem Ipsum has been the industry's standard dummy text ever since the 1500s, when an unknown printer took a galley of type and scrambled it to make a type specimen book. It has survived not only five centuries, but also the leap into electronic typesetting, remaining essentially unchanged. It was popularised in the 1960s with the release of transfer sheets containing Lorem Ipsum</p>
  <a class="more" style="margin-right:0">Read More...</a>
</section>

<footer>
  <div class="abs footer"></div>
  <div class="abs divider" style="left:408px"></div>
  <div class="abs divider" style="left:782px"></div>
  <section class="abs" style="left:72px;top:767px;width:312px">
    <div class="foot-h">ABOUT US</div>
    <p class="foot-txt" style="margin-top:5px">The standard chunk of Lorem Ipsum used since the 1500s is reproduced below for those interested. Sections 1.10.32 and 1.10.33 from "de Finibus Bonorum et Malorum" by an early author are also reproduced in their exact original form, accompanied by English versions from the 1914 translation by a later scholar.</p>
    <a class="more dim" style="margin-top:8px">Read More...</a>
  </section>
  <section class="abs" style="left:441px;top:767px;width:320px">
    <div class="foot-h">WHAT PEOPLE SAY ABOUT US</div>
    <div class="quote-name" style="margin-top:6px">Daniel Mercer<small>Vestiblue Molesim Blaca</small></div>
    <p class="foot-txt">« Lorem Ipsum has been the industry's standard dummy text ever since the 1500s.»</p>
    <div class="quote-name">Paul Hadley<small>Vestiblue Molesim Blaca</small></div>
    <p class="foot-txt">« Lorem Ipsum has been the industry's standard dummy text ever since the 1500s.»</p>
  </section>
  <section class="abs" style="left:813px;top:767px;width:300px">
    <div class="foot-h">OUR ADDRESS</div>
    <p class="foot-txt" style="margin-top:5px;text-align:left">420, Dummy Street,<br>Opp. Lorem Ipsum Avenue, Main Road,<br>Washington DC, USA.<br>Phone : +1234567890,<br>E-mail : info@meridianbrokerage.com</p>
    <div style="font-size:9px;line-height:10px;color:#333;margin-top:3px;letter-spacing:.4px">Follow Us At:</div>
    <div class="social"><span class="on"></span><span></span><span></span></div>
    <div class="fan">Become a Fan On<br>Our Page</div>
  </section>
  <div class="abs copyright">© Copyrights 2013. All Rights Reserved.</div>
  <div class="abs foot-brand">Meridian</div>
</footer>
</body>
</html>
```